ARC VOLLEY Business Card Project

I'd like to request a business card design for the new company I've launched.
The name of the company is "ARC VOLLEY" an indoor unmanned tennis practice facility.
We would like to see designs that use our brand identity color in the logo I've attached.
We hope to get the design with modern, luxurious and elegant tone and manner.
We hope the logo should not be too big.

Business card must have elements as below:
- Logo (One of the logos I've attached)
- Name (In Korean Text) : 박 서 윤
- Title (In Korean Text) : 대표
- Phone Number : 010-8472-3916
- Email Address : seoyun.park@arcvolley-example.co.kr
- Website : www.arcvolley-example.co.kr
- Instagram : arcvolley
- Address (In Korean text) : 경기도 용인시 수지구 풍덕천로 456 미래타워 5층 501호, 502호

Target Market(s)

Tennis amateurs in 20 to 40s

Industry/Entity Type

Sports, Hobby

Contact Information for Business Card

- Logo (One of the logos I've attached) - Name (In Korean Text) : 박 서 윤 - Title (In Korean Text) : 대표 - Phone Number : 010-8472-3916 - Email Address : seoyun.park@arcvolley-example.co.kr - Website : www.arcvolley-example.co.kr - Instagram : arcvolley - Address (In Korean text) : 경기도 용인시 수지구 풍덕천로 456 미래타워 5층 501호, 502호

Font styles to use
Sans Serif

Requirements
Must have
• Double sided
Nice to have
• Logo with intaglio or relief embossing
Should not have
• Logo should not be too big.

```html
<!DOCTYPE html>
<html lang="ko">
<head>
<meta charset="utf-8">
<title>ARC VOLLEY Business Card</title>
<link rel="stylesheet" href="https://fonts.googleapis.com/css2?family=Cinzel:wght@400;600&family=Noto+Sans+KR:wght@400;700&display=swap">
<style>
  :root {
    --bg: #dcdcdc;
    --brand-green: #2d5139;
    --ink: #1a1a1a;
    --slate: #4a4a4a;
    --muted: #666666;
    --paper: #ffffff;
  }
  * { box-sizing: border-box; margin: 0; padding: 0; }
  html, body { width: 1200px; height: 780px; overflow: hidden; background: var(--bg); }
  .canvas { position: relative; width: 1200px; height: 780px; }

  .card {
    position: absolute;
    width: 560px;
    height: 320px;
    border-radius: 28px;
    overflow: hidden;
    box-shadow: 0 10px 24px rgba(0,0,0,0.28);
  }

  /* Front */
  .card-front { left: 140px; top: 60px; background: var(--brand-green); }
  .front-brand {
    position: absolute; inset: 0;
    display: flex; align-items: center; justify-content: center; gap: 16px;
  }
  .brand-dot { width: 48px; height: 48px; border-radius: 50%; }
  .card-front .brand-dot { background: var(--paper); }
  .brand-name {
    font-family: "Cinzel", serif;
    font-weight: 400;
    letter-spacing: 0.02em;
    white-space: nowrap;
  }
  .card-front .brand-name { color: var(--paper); font-size: 36px; }

  /* Back */
  .card-back { left: 500px; top: 400px; background: var(--paper); }
  .back-shapes { position: absolute; inset: 0; }
  .band-green { fill: var(--brand-green); }
  .band-slate { fill: var(--slate); }
  .divider { stroke: var(--slate); stroke-width: 1.2; }

  .back-brand {
    position: absolute; left: 20px; top: 70px; width: 230px;
    display: flex; flex-direction: column; align-items: center; gap: 14px;
  }
  .card-back .brand-dot { width: 74px; height: 74px; background: var(--brand-green); }
  .card-back .brand-name { color: var(--brand-green); font-size: 27px; }

  .person { position: absolute; left: 292px; top: 42px; }
  .person-name {
    font-family: "Noto Sans KR", sans-serif; font-weight: 700;
    font-size: 34px; letter-spacing: 0.08em; color: var(--brand-green); line-height: 1.1;
  }
  .person-title {
    font-family: "Noto Sans KR", sans-serif; font-weight: 400;
    font-size: 17px; color: var(--muted); margin-top: 2px;
  }

  .contacts { position: absolute; left: 292px; top: 140px; list-style: none; }
  .contacts li {
    display: flex; align-items: center; gap: 7px; height: 19px;
    font-family: "Cinzel", serif; font-size: 9.5px; color: var(--ink); white-space: nowrap;
  }
  .contacts svg { width: 11px; height: 11px; flex: none; }
  .icon-fill { fill: var(--brand-green); }
  .icon-line { fill: none; stroke: var(--brand-green); stroke-width: 1.6; }

  .address {
    position: absolute; left: 36px; top: 240px;
    font-family: "Noto Sans KR", sans-serif; font-weight: 700;
    font-size: 13px; color: var(--ink); white-space: nowrap;
  }
</style>
</head>
<body>
<main class="canvas">

  <section class="card card-front" aria-label="Business card front">
    <div class="front-brand">
      <span class="brand-dot"></span>
      <span class="brand-name">ARC VOLLEY</span>
    </div>
  </section>

  <section class="card card-back" aria-label="Business card back">
    <svg class="back-shapes" viewBox="0 0 560 320" width="560" height="320" aria-hidden="true">
      <line class="divider" x1="250" y1="40" x2="275" y2="222"/>
      <polygon class="band-slate" points="335,268 560,268 560,320 363,320"/>
      <polygon class="band-green" points="0,290 335,290 357,320 0,320"/>
    </svg>

    <div class="back-brand">
      <span class="brand-dot"></span>
      <span class="brand-name">ARC VOLLEY</span>
    </div>

    <div class="person">
      <p class="person-name">박 서 윤</p>
      <p class="person-title">대표</p>
    </div>

    <ul class="contacts">
      <li>
        <svg viewBox="0 0 12 12"><path class="icon-fill" d="M2.5 1 L4.6 1 L5.3 3.6 L4 4.6 C4.6 6 5.9 7.4 7.4 8 L8.4 6.7 L11 7.4 L11 9.5 C11 10.3 10.3 11 9.5 11 C5 11 1 7 1 2.5 C1 1.7 1.7 1 2.5 1 Z"/></svg>
        010-8472-3916
      </li>
      <li>
        <svg viewBox="0 0 12 12"><circle class="icon-fill" cx="6" cy="6" r="3"/></svg>
        ARCVOLLEY
      </li>
      <li>
        <svg viewBox="0 0 12 12"><circle class="icon-line" cx="6" cy="6" r="4.6"/><path class="icon-line" d="M1.4 6 H10.6 M6 1.4 C3.6 4 3.6 8 6 10.6 M6 1.4 C8.4 4 8.4 8 6 10.6"/></svg>
        WWW.ARCVOLLEY-EXAMPLE.CO.KR
      </li>
      <li>
        <svg viewBox="0 0 12 12"><rect class="icon-line" x="1.3" y="2.6" width="9.4" height="6.8" rx="1"/><path class="icon-line" d="M1.6 3 L6 6.6 L10.4 3"/></svg>
        SEOYUN.PARK@ARCVOLLEY-EXAMPLE.CO.KR
      </li>
    </ul>

    <p class="address">경기도 용인시 수지구 풍덕천로 456 미래타워 5층 501호, 502호</p>
  </section>

</main>
</body>
</html>
```